New webpage design for development bureau

We are a development bureau in Denmark, and need a design for our webpage. We are called Harbor Development (Part of Harbor Fjeld Skolium Group), and are going to aim for multiple markets: Web, Apps, Desktop applications, ect.

We already have a logo, see the uploaded file. We do not have any special demands, other than in have to be simple. A portfolio view should also be available, for future customers.

```html
<!DOCTYPE html>
<html lang="en">
<head>
<meta charset="utf-8">
<title>Harbor Development</title>
<link href="https://fonts.googleapis.com/css2?family=Dosis:wght@300;400;600;700&family=Open+Sans:wght@400;600;700&display=swap" rel="stylesheet">
<style>
:root{
  --green:#1ba57a;
  --green-dark:#148a65;
  --ink:#222;
  --text:#666;
  --muted:#999;
  --dark:#1d1d1d;
  --darker:#121212;
  --band:#e4e4e4;
  --white:#fff;
}
*{box-sizing:border-box;margin:0;padding:0}
html,body{width:1200px;height:2664px;overflow:hidden}
body{position:relative;background:var(--white);font-family:"Open Sans",sans-serif;color:var(--text);font-size:12px;line-height:1.55}
.abs{position:absolute}
h1,h2,h3,h4,.nav a,.caps{font-family:"Dosis",sans-serif}

/* header */
.site-header{position:absolute;left:0;top:0;width:1200px;height:140px;background:var(--white)}
.brand{left:180px;top:38px;display:flex;align-items:center;gap:10px;font-family:"Dosis",sans-serif;font-weight:700;font-size:34px;color:var(--ink);letter-spacing:1px}
.nav{left:500px;top:64px;display:flex;gap:34px}
.nav a{font-size:14px;font-weight:600;color:var(--ink);text-decoration:none;letter-spacing:.5px;padding-bottom:10px}
.nav a.active{color:var(--green);border-bottom:3px solid var(--green)}
.social{left:915px;top:20px;display:flex;gap:6px}
.social span{width:24px;height:24px;background:#8a9aa8;display:block}

/* hero */
.hero{left:0;top:140px;width:1200px;height:460px;background:linear-gradient(100deg,#d7dde2 0%,#eef1f3 35%,#cfd6dc 60%,#aab3ba 100%)}
.hero-caption{left:0;top:392px;width:1200px;height:108px;background:rgba(255,255,255,.62)}
.hero-title{left:180px;top:412px;font-size:20px;font-weight:600;color:var(--ink);letter-spacing:.5px}
.hero-title em{font-style:normal;color:var(--green)}
.hero-tags{left:180px;top:454px;font-size:14px;font-weight:600;color:var(--ink);display:flex;gap:10px;align-items:center}
.hero-tags .tag-hi{background:var(--green);color:var(--white);padding:3px 10px}

/* welcome */
.welcome-title{left:180px;top:648px;font-size:30px;font-weight:400;color:var(--ink);letter-spacing:2px;line-height:1}
.welcome-name{left:180px;top:678px;font-size:66px;font-weight:300;color:var(--green);letter-spacing:3px;line-height:1}
.welcome-text{left:180px;top:760px;width:390px;font-size:12px}
.welcome-text p{margin-bottom:8px}
.service{width:210px;text-align:center}
.service svg{display:block;margin:0 auto 6px}
.service h4{font-size:15px;font-weight:700;color:var(--ink);letter-spacing:.5px;margin-bottom:4px}
.service p{font-size:11px;line-height:1.5}

/* process band */
.process{left:0;top:960px;width:1200px;height:240px;background:var(--dark)}
.step{top:30px;width:260px;text-align:center;color:#bbb}
.step .ring{width:86px;height:86px;border-radius:50%;border:2px solid #888;margin:0 auto 10px;display:flex;align-items:center;justify-content:center}
.step h4{color:var(--white);font-size:18px;font-weight:700;letter-spacing:.5px;margin-bottom:6px}
.step p{font-size:11px;line-height:1.5}

/* portfolio */
.sec-small{left:180px;font-size:30px;font-weight:400;color:var(--ink);letter-spacing:2px;line-height:1}
.sec-big{left:180px;font-size:60px;font-weight:300;color:var(--green);letter-spacing:3px;line-height:1}
.filters{left:595px;top:1287px;display:flex;gap:28px;font-size:13px;color:var(--muted)}
.filters .on{color:var(--ink);font-weight:700}
.portfolio-band{left:0;top:1322px;width:1200px;height:508px;background:var(--band)}
.arrow{top:1548px;width:48px;height:48px;border-radius:50%;border:2px solid #777;display:flex;align-items:center;justify-content:center;background:var(--white)}
.tile{display:block}

/* news */
.news-card{top:1978px;width:195px}
.news-img{height:120px}
.news-date{font-size:10px;color:var(--muted);margin-top:8px}
.news-card h3{font-family:"Open Sans",sans-serif;font-size:13px;font-weight:600;color:var(--green);line-height:1.35;margin:4px 0 6px}
.news-card p{font-size:11px;line-height:1.5}
.btn{display:inline-block;background:var(--green);color:var(--white);font-size:10px;font-weight:700;padding:7px 20px;letter-spacing:.5px;margin-top:12px}
.timeline{left:180px;top:2330px;width:840px;height:2px;background:#cfcfcf}
.dot{top:2325px;width:12px;height:12px;border-radius:50%;background:var(--green)}

/* footer */
.site-footer{left:0;top:2392px;width:1200px;height:208px;background:var(--dark)}
.foot-h{font-size:17px;font-weight:700;color:var(--white);letter-spacing:.5px}
.map{left:180px;top:2440px;width:250px;height:140px;background:linear-gradient(120deg,#2b2b2b,#3a3a3a 50%,#2a2a2a)}
.contact{left:190px;font-size:11px;color:#ccc;display:flex;align-items:center;gap:10px}
.contact svg{flex:none}
.field{background:transparent;border:1px solid #555;color:#aaa;font-size:11px;padding:8px 10px}
.send{left:910px;top:2522px;width:110px;height:30px;background:var(--green);color:var(--white);font-size:11px;font-weight:700;text-align:center;line-height:30px}
.bottom-bar{left:0;top:2600px;width:1200px;height:64px;background:var(--darker);font-size:11px;color:#aaa}
</style>
</head>
<body>

<header class="site-header">
  <div class="abs brand"><span>HARBOR</span></div>
  <div class="abs social"><span></span><span></span><span></span><span></span></div>
  <nav class="abs nav">
    <a class="active">HOME</a><a>ABOUT US</a><a>SERVICES</a><a>WORKS</a><a>CONTACT US</a><a>BLOG</a>
  </nav>
</header>

<div class="abs hero" role="img" aria-label="Photo of a smiling man in an office holding a tablet"></div>
<div class="abs hero-caption"></div>
<div class="abs hero-title">LOREM IPSUM DOLOR SIT AMET, <em>CONSECTETUR ADIPISCING ELIT</em></div>
<div class="abs hero-tags"><span>DEVELOPMENT</span><span>.</span><span>WEB</span><span>.</span><span>APPS</span><span>.</span><span class="tag-hi">DESKTOP APPLICATION</span></div>

<section>
  <h2 class="abs welcome-title">WELCOME TO</h2>
  <h1 class="abs welcome-name">HARBOR</h1>
  <div class="abs welcome-text">
    <p>Lorem ipsum dolor sit amet, consectetur adipiscing elit, sed diam nonummy nibh euismod tincidunt ut laoreet dolore magna aliquam erat volutpat. Ut wisi enim ad minim veniam, quis nostrud exerci tation ullamcorper suscipit lobortis nisl ut aliquip ex ea commodo consequat.</p>
    <p>Duis autem vel eum iriure dolor in hendrerit in vulputate velit esse molestie consequat, vel illum dolore eu feugiat nulla facilisis at vero eros et accumsan et iusto odio dignissim qui blandit praesent luptatum zzril delenit augue duis dolore te feugait nulla facilisi.</p>
  </div>

  <div class="abs service" style="left:600px;top:655px">
    <svg width="40" height="40" viewBox="0 0 40 40"><rect x="6" y="8" width="28" height="24" rx="2" fill="none" stroke="#222" stroke-width="2.5"/><line x1="6" y1="14" x2="34" y2="14" stroke="#222" stroke-width="2.5"/><circle cx="20" cy="23" r="5" fill="none" stroke="#222" stroke-width="2"/></svg>
    <h4>WEB</h4>
    <p>Typo text between standard sites and<br>simple web layouts for everyone.</p>
  </div>
  <div class="abs service" style="left:820px;top:655px">
    <svg width="40" height="40" viewBox="0 0 40 40"><rect x="12" y="5" width="16" height="30" rx="2" fill="none" stroke="#222" stroke-width="2.5"/><line x1="17" y1="30" x2="23" y2="30" stroke="#222" stroke-width="2"/><rect x="22" y="10" width="12" height="10" fill="#fff" stroke="#222" stroke-width="2"/></svg>
    <h4>APPS</h4>
    <p>Typo text between standard apps and<br>mobile tools for every device.</p>
  </div>
  <div class="abs service" style="left:710px;top:800px">
    <svg width="40" height="40" viewBox="0 0 40 40"><rect x="6" y="8" width="28" height="18" rx="1" fill="none" stroke="#222" stroke-width="2.5"/><line x1="20" y1="26" x2="20" y2="32" stroke="#222" stroke-width="2.5"/><line x1="13" y1="33" x2="27" y2="33" stroke="#222" stroke-width="2.5"/></svg>
    <h4>DESKTOP APPLICATIONS</h4>
    <p>Typo text between desktop programs and<br>tools built for office work.</p>
  </div>
</section>

<section class="abs process">
  <div class="abs step" style="left:180px">
    <div class="ring"><svg width="34" height="34" viewBox="0 0 34 34"><rect x="5" y="7" width="24" height="22" rx="2" fill="none" stroke="#fff" stroke-width="2.5"/><line x1="5" y1="13" x2="29" y2="13" stroke="#fff" stroke-width="2.5"/><line x1="11" y1="4" x2="11" y2="9" stroke="#fff" stroke-width="2.5"/><line x1="23" y1="4" x2="23" y2="9" stroke="#fff" stroke-width="2.5"/></svg></div>
    <h4>PLANNING</h4>
    <p>Team brief about the project, planning the work and setting a clear goal together with the client before any line is written.</p>
  </div>
  <div class="abs step" style="left:470px">
    <div class="ring"><svg width="34" height="34" viewBox="0 0 34 34"><line x1="7" y1="7" x2="27" y2="27" stroke="#fff" stroke-width="3"/><line x1="27" y1="7" x2="7" y2="27" stroke="#fff" stroke-width="3"/></svg></div>
    <h4>DESIGN</h4>
    <p>Clean and simple layouts drawn for the user, tested early and shaped with the client until every screen feels right.</p>
  </div>
  <div class="abs step" style="left:760px">
    <div class="ring"><svg width="34" height="34" viewBox="0 0 34 34"><rect x="5" y="7" width="24" height="16" fill="none" stroke="#fff" stroke-width="2.5"/><line x1="17" y1="23" x2="17" y2="28" stroke="#fff" stroke-width="2.5"/><line x1="10" y1="29" x2="24" y2="29" stroke="#fff" stroke-width="2.5"/></svg></div>
    <h4>DEVELOPMENT</h4>
    <p>Solid code for web, apps and desktop, delivered in small steps and kept stable long after the launch day.</p>
  </div>
</section>

<section>
  <h2 class="abs sec-small" style="top:1222px">OUR</h2>
  <h2 class="abs sec-big" style="top:1252px">PORTFOLIO</h2>
  <div class="abs filters"><span class="on">ALL</span><span>WEB</span><span>APPS</span><span>DESKTOP APPLICATION</span></div>
  <div class="abs portfolio-band"></div>
  <div class="abs tile" style="left:180px;top:1332px;width:270px;height:225px;background:linear-gradient(160deg,#c8d3dc,#7a8b99)" role="img" aria-label="Project image: person working on a laptop outdoors"></div>
  <div class="abs tile" style="left:460px;top:1332px;width:320px;height:225px;background:linear-gradient(160deg,#2ec79a,#0e8a66)" role="img" aria-label="Project image: green illustration with a small figure"></div>
  <div class="abs tile" style="left:790px;top:1332px;width:230px;height:225px;background:linear-gradient(160deg,#f4f4f4,#d9d4cc)" role="img" aria-label="Project image: colourful paper shapes on white"></div>
  <div class="abs tile" style="left:180px;top:1567px;width:270px;height:253px;background:linear-gradient(160deg,#6a5a50,#2c2622)" role="img" aria-label="Project image: dramatic dark portrait scene"></div>
  <div class="abs tile" style="left:460px;top:1567px;width:320px;height:253px;background:linear-gradient(180deg,#8fc6ef,#2f7fbf 55%,#5a8f3a)" role="img" aria-label="Project image: floating green island in a blue sky"></div>
  <div class="abs tile" style="left:790px;top:1567px;width:230px;height:120px;background:linear-gradient(160deg,#aac4dc,#6f8ea9)" role="img" aria-label="Project image: city buildings under a sky"></div>
  <div class="abs tile" style="left:790px;top:1697px;width:230px;height:123px;background:linear-gradient(160deg,#d8dde2,#8e9aa4)" role="img" aria-label="Project image: pale landscape scene"></div>
  <div class="abs arrow" style="left:76px"><svg width="20" height="20" viewBox="0 0 20 20"><path d="M13 3 L6 10 L13 17" fill="none" stroke="#444" stroke-width="2.5"/></svg></div>
  <div class="abs arrow" style="left:1076px"><svg width="20" height="20" viewBox="0 0 20 20"><path d="M7 3 L14 10 L7 17" fill="none" stroke="#444" stroke-width="2.5"/></svg></div>
</section>

<section>
  <h2 class="abs sec-small" style="top:1862px">LATEST</h2>
  <h2 class="abs sec-big" style="top:1892px">NEWS</h2>

  <article class="abs news-card" style="left:180px">
    <div class="news-img" style="background:linear-gradient(160deg,#dfe6ec,#9fb0bd)" role="img" aria-label="News image: person holding colourful umbrella"></div>
    <div class="news-date">12 MAY, 2014</div>
    <h3>Nam liber tempor cum soluta nobis eleifend option</h3>
    <p>Lorem ipsum dolor sit amet, consectetur adipiscing elit sed diam nonummy nibh euismod tincidunt.</p>
    <span class="btn">READ MORE</span>
  </article>
  <article class="abs news-card" style="left:395px">
    <div class="news-img" style="background:linear-gradient(160deg,#9dc8ea,#3f7fb4)" role="img" aria-label="News image: figure leaping under a blue sky"></div>
    <div class="news-date">09 MAY, 2014</div>
    <h3>Typi non habent claritatem insitam est usus</h3>
    <p>Lorem ipsum dolor sit amet, consectetur adipiscing elit sed diam nonummy nibh euismod tincidunt.</p>
    <span class="btn">READ MORE</span>
  </article>
  <article class="abs news-card" style="left:610px">
    <div class="news-img" style="background:linear-gradient(160deg,#6b6b6b,#2b2b2b)" role="img" aria-label="News image: dark scene with a person and a bicycle"></div>
    <div class="news-date">05 MAY, 2014</div>
    <h3>Lorem ipsum dolor sit amet consectetuer adipiscing</h3>
    <p>Lorem ipsum dolor sit amet, consectetur adipiscing elit sed diam nonummy nibh euismod tincidunt.</p>
    <span class="btn">READ MORE</span>
  </article>
  <article class="abs news-card" style="left:825px">
    <div class="news-img" style="background:linear-gradient(160deg,#c9ced3,#7d868e)" role="img" aria-label="News image: person with umbrella in grey weather"></div>
    <div class="news-date">01 MAY, 2014</div>
    <h3>Duis autem vel eum iriure dolor in hendrerit</h3>
    <p>Lorem ipsum dolor sit amet, consectetur adipiscing elit sed diam nonummy nibh euismod tincidunt.</p>
    <span class="btn">READ MORE</span>
  </article>

  <div class="abs timeline"></div>
  <div class="abs dot" style="left:200px"></div>
  <div class="abs dot" style="left:330px"></div>
  <div class="abs dot" style="left:460px"></div>
  <div class="abs dot" style="left:590px"></div>
  <div class="abs dot" style="left:720px"></div>
  <div class="abs dot" style="left:850px"></div>
  <div class="abs dot" style="left:980px"></div>
</section>

<footer>
  <div class="abs site-footer"></div>
  <div class="abs foot-h" style="left:180px;top:2410px">GET IN TOUCH</div>
  <div class="abs map" role="img" aria-label="Faint world map behind contact details"></div>
  <div class="abs contact" style="top:2448px"><svg width="14" height="14" viewBox="0 0 14 14"><path d="M7 1a4 4 0 0 1 4 4c0 3-4 8-4 8S3 8 3 5a4 4 0 0 1 4-4z" fill="#1ba57a"/></svg><span>Harbor Development, Havnegade 12<br>1058 Copenhagen, Denmark</span></div>
  <div class="abs contact" style="top:2500px"><svg width="14" height="14" viewBox="0 0 14 14"><path d="M3 1h3l1 3-2 1.5a7 7 0 0 0 3.5 3.5L10 7l3 1v3c0 1-1 2-2 2C6 13 1 8 1 3c0-1 1-2 2-2z" fill="#1ba57a"/></svg><span>+45 31 42 58 76</span></div>
  <div class="abs contact" style="top:2530px"><svg width="14" height="14" viewBox="0 0 14 14"><rect x="1" y="3" width="12" height="8" fill="#1ba57a"/><path d="M1 3l6 5 6-5" fill="none" stroke="#1d1d1d" stroke-width="1.2"/></svg><span>hello@harbordev.dk</span></div>

  <div class="abs foot-h" style="left:480px;top:2410px">SEND MAIL</div>
  <div class="abs field" style="left:480px;top:2442px;width:260px;height:32px">Name</div>
  <div class="abs field" style="left:760px;top:2442px;width:260px;height:32px">Email Address</div>
  <div class="abs field" style="left:480px;top:2484px;width:410px;height:80px">Message</div>
  <div class="abs send caps">SEND</div>

  <div class="abs bottom-bar">
    <span class="abs" style="left:180px;top:24px">Privacy Policy</span>
    <span class="abs" style="left:275px;top:24px">Sitemap</span>
    <span class="abs" style="left:820px;top:24px">Copyright@2014. All Right Reserved.</span>
  </div>
</footer>

</body>
</html>
```